Business card design needed

New company based in Brisbane, Australia. Brindle Systems. The business is focused on the delivery of network architecture design and deployment. We will provide both services and the sale of the necessary equipment to deliver the service. Cloud computing is an important element of our focus as this is an emerging market for enterprises in Queensland. Our target marketplace is medium to large corporations with complex infrastructure requirements. IT Management and above will be the typical entry point for us into these accounts. We would like to see the use of various shade of green, design should be clutter free and impress stability, trust and growth.
Updates
Hey Everyone
Just we let you all know we have changed this project to 'committed' payment status.
Looking forward to seeing the designs! Thanks for your efforts.
Best Regards
Marcus
Industry/Entity Type
Architecture
Contact Information for Business Card
Brindle Systems, Marcus Doyle, Sales Director, Level 14 Harlow Tower, 58 Penfold Street, Brisbane QLD 4000, Ph +61 7 3904 2267, M +61 4 4926 1573, E marcus.doyle@brindlesystems-example.com.au
Look and feel
Each slider illustrates characteristics of the customer's brand and the style your logo design should communicate.

```html
<!DOCTYPE html>
<html lang="en">
<head>
<meta charset="utf-8">
<title>Brindle Systems — Business Card</title>
<link rel="stylesheet" href="https://fonts.googleapis.com/css2?family=Arimo:wght@400&display=swap">
<style>
  :root {
    --card-bg: #e6ebe8;
    --panel-bg: #f3f6f4;
    --name-green: #1e8a1e;
    --title-green: #55e02a;
    --brand-green: #24b324;
    --contact-green: #22a322;
    --address-green: #2a9a2a;
  }
  * { margin: 0; padding: 0; box-sizing: border-box; }
  html, body {
    width: 1200px;
    height: 741px;
    overflow: hidden;
    background: var(--card-bg);
  }
  .card {
    position: relative;
    width: 1200px;
    height: 741px;
    background: var(--card-bg);
    font-family: "Arimo", Arial, Helvetica, sans-serif;
  }
  .brand-panel {
    position: absolute;
    left: 0;
    top: 45px;
    width: 571px;
    height: 240px;
    background: var(--panel-bg);
    display: flex;
    align-items: center;
    padding-left: 51px;
    gap: 22px;
  }
  .brand-mark { flex: none; }
  .brand-name {
    font-size: 47px;
    font-weight: 400;
    color: var(--brand-green);
    white-space: nowrap;
    letter-spacing: -0.5px;
  }
  .person {
    position: absolute;
    left: 571px;
    right: 0;
    top: 88px;
    text-align: center;
  }
  .person-name {
    font-size: 65px;
    color: var(--name-green);
    line-height: 1;
    font-weight: 400;
  }
  .person-title {
    margin-top: 28px;
    font-size: 52px;
    color: var(--title-green);
    line-height: 1;
    font-weight: 400;
  }
  .contacts {
    position: absolute;
    left: 45px;
    top: 368px;
    color: var(--contact-green);
    list-style: none;
  }
  .contacts li { line-height: 1; white-space: nowrap; }
  .contact-phone { font-size: 54px; }
  .contact-mobile { font-size: 54px; margin-top: 21px; }
  .contact-email { font-size: 42px; margin-top: 25px; padding-left: 4px; }
  .address {
    position: absolute;
    left: 0;
    right: 0;
    top: 672px;
    text-align: center;
    padding-right: 5px;
    font-size: 32px;
    color: var(--address-green);
    line-height: 1;
    font-style: normal;
  }
</style>
</head>
<body>
  <div class="card">
    <div class="brand-panel">
      <svg class="brand-mark" width="92" height="92" viewBox="0 0 92 92" aria-hidden="true">
        <circle cx="46" cy="46" r="46" fill="var(--brand-green)"/>
      </svg>
      <span class="brand-name">Brindle Systems</span>
    </div>

    <div class="person">
      <h1 class="person-name">Marcus Doyle</h1>
      <p class="person-title">Sales Director</p>
    </div>

    <ul class="contacts">
      <li class="contact-phone">P: +61 7 3904 2267</li>
      <li class="contact-mobile">M: +61 4 4926 1573</li>
      <li class="contact-email">E: marcus.doyle@brindlesystems-example.com.au</li>
    </ul>

    <address class="address">Level 14 Harlow Tower, 58 Penfold Street, Brisbane QLD 4000</address>
  </div>
</body>
</html>
```